Forest Consultant/Timber Buyer needs a clean business card

We are a forestry consulting and timber buying company. We meet with private landowners and assist them with timber management and timber harvesting. We would like a professional business card, please no clip art. logo is blue and white but would like to see a gray,silver, or some other color incorporated. Would like basic contact info. Would like to the layout to be creative and sleek but masculine.

Target Market(s)

private landowners

Industry/Entity Type

Business

Contact Information for Business Card

name,position, cell number, office number, email, website. This might be to cluttered. Basic contact info is what we are looking for.

Contact info can all be on one side with logo on the other.

Font styles to use
Serif
Sans Serif

Colors
0255a3
ffffff
aaaaaa

Requirements
Must have
• We just want it professional.
Nice to have
• Creative layout.
Should not have
• please no clip art of log trucks etc.

```html
<!DOCTYPE html>
<html lang="en">
<head>
<meta charset="utf-8">
<title>Cedarvale Land &amp; Timber – Business Card</title>
<link href="https://fonts.googleapis.com/css2?family=Open+Sans:wght@400;600&display=swap" rel="stylesheet">
<style>
  :root {
    --brand-blue: #0255a3;
    --white: #ffffff;
    --silver: #aaaaaa;
    --card-black: #111213;
    --backdrop: #3d3634;
  }
  * { margin: 0; padding: 0; box-sizing: border-box; }
  html, body { width: 1200px; height: 814px; overflow: hidden; }
  body {
    background: var(--backdrop);
    font-family: "Open Sans", Arial, sans-serif;
    position: relative;
  }
  .card {
    position: absolute;
    width: 525px;
    height: 300px;
    background: var(--card-black);
    border-radius: 3px;
    box-shadow: 0 6px 18px rgba(0,0,0,.45);
    overflow: hidden;
  }
  .card--contact { left: 50px; top: 320px; }
  .card--brand { left: 625px; top: 120px; }

  /* contact side */
  .brand-mark {
    position: absolute;
    left: 40px; top: 100px;
    width: 200px;
    display: flex; align-items: center; gap: 10px;
  }
  .brand-mark__dot {
    width: 18px; height: 18px; border-radius: 50%;
    background: var(--brand-blue); flex: none;
  }
  .brand-mark__name {
    color: var(--brand-blue);
    font-weight: 600; font-size: 19px; line-height: 1.25;
  }
  .divider {
    position: absolute; left: 262px; top: 52px;
    width: 1px; height: 196px;
    background: linear-gradient(var(--silver), rgba(170,170,170,.2));
  }
  .contact { position: absolute; left: 285px; top: 54px; }
  .contact__name { color: var(--brand-blue); font-size: 17px; font-weight: 600; line-height: 1.2; }
  .contact__role { color: var(--white); font-size: 13px; margin-bottom: 14px; }
  .contact__list { list-style: none; }
  .contact__item {
    display: flex; align-items: center; gap: 9px;
    color: var(--white); font-size: 13px; line-height: 21px;
  }
  .contact__item svg { width: 12px; height: 12px; fill: var(--brand-blue); flex: none; }

  /* brand side */
  .brand-lockup {
    position: absolute; left: 0; right: 0; top: 105px;
    display: flex; justify-content: center; align-items: center; gap: 14px;
  }
  .brand-lockup__dot {
    width: 26px; height: 26px; border-radius: 50%;
    background: var(--brand-blue);
  }
  .brand-lockup__name {
    color: var(--brand-blue); font-weight: 600; font-size: 28px; letter-spacing: 1px;
  }
  .brand-web {
    position: absolute; left: 0; right: 0; top: 200px;
    text-align: center; color: var(--white);
    font-size: 12px; letter-spacing: 3px;
  }
</style>
</head>
<body>
  <section class="card card--contact">
    <div class="brand-mark">
      <span class="brand-mark__dot"></span>
      <span class="brand-mark__name">Cedarvale Land &amp; Timber</span>
    </div>
    <div class="divider"></div>
    <div class="contact">
      <p class="contact__name">Mark Holden</p>
      <p class="contact__role">CEO/Founder</p>
      <ul class="contact__list">
        <li class="contact__item">
          <svg viewBox="0 0 24 24"><path d="M6.6 10.8a15 15 0 0 0 6.6 6.6l2.2-2.2a1 1 0 0 1 1-.25 11.4 11.4 0 0 0 3.6.57 1 1 0 0 1 1 1V20a1 1 0 0 1-1 1A17 17 0 0 1 3 4a1 1 0 0 1 1-1h3.5a1 1 0 0 1 1 1c0 1.25.2 2.45.57 3.57a1 1 0 0 1-.25 1z"/></svg>
          555 214 0387
        </li>
        <li class="contact__item">
          <svg viewBox="0 0 24 24"><path d="M7 1h10a2 2 0 0 1 2 2v18a2 2 0 0 1-2 2H7a2 2 0 0 1-2-2V3a2 2 0 0 1 2-2zm0 3v14h10V4z"/></svg>
          555 730 6142
        </li>
        <li class="contact__item">
          <svg viewBox="0 0 24 24"><path d="M2 5h20v14H2zm2 2v.5l8 5 8-5V7z"/></svg>
          info@cedarvale.com
        </li>
        <li class="contact__item">
          <svg viewBox="0 0 24 24"><path d="M12 2a10 10 0 1 0 0 20 10 10 0 0 0 0-20zm1 17.9V18h-2v1.9A8 8 0 0 1 4.1 13H6v-2H4.1A8 8 0 0 1 11 4.1V6h2V4.1a8 8 0 0 1 6.9 6.9H18v2h1.9a8 8 0 0 1-6.9 6.9z"/></svg>
          www.cedarvale.com
        </li>
      </ul>
    </div>
  </section>

  <section class="card card--brand">
    <div class="brand-lockup">
      <span class="brand-lockup__dot"></span>
      <span class="brand-lockup__name">Cedarvale Land &amp; Timber</span>
    </div>
    <p class="brand-web">www.cedarvale.com</p>
  </section>
</body>
</html>
```